Redesign of an insurance website

Attached is an insurance website that I need to redesign. Currently the website is too dark. I like for example www.brenvalo.com . Could you make the website lighter and change the structure a little so that it is more user friendly?

Industry/Entity Type

Insurance

Number of Pages Required

4 page

```html
<!DOCTYPE html>
<html lang="cs">
<head>
<meta charset="utf-8">
<title>Krytona – Najdete nejvyhodnejsi pojisteni</title>
<link href="https://fonts.googleapis.com/css2?family=Lato:wght@400;700&family=Montserrat:wght@600;700&family=Quicksand:wght@400;500&display=swap" rel="stylesheet">
<style>
  :root{
    --brand:#2f86f6;
    --ink:#1d1f22;
    --ink-soft:#8a8a8a;
    --navy:#232b34;
    --line:#e3e3e3;
    --white:#ffffff;
    --tile-blue:#3a7bd5;
    --tile-yellow:#f9b41a;
    --tile-purple:#a995cf;
    --tile-sky:#5b9bd8;
  }
  *{box-sizing:border-box;margin:0;padding:0}
  html,body{width:1200px;height:906px;overflow:hidden;background:var(--white)}
  body{font-family:"Lato",sans-serif;color:var(--ink);position:relative}

  .site-header{position:absolute;left:0;top:0;width:1200px;height:102px}
  .social{position:absolute;left:70px;top:40px;display:flex;gap:12px}
  .social span{width:20px;height:20px;border-radius:50%;background:var(--ink)}
  .brand{position:absolute;left:0;width:1200px;top:33px;text-align:center;font-family:"Lato",sans-serif;font-weight:700;font-size:30px;letter-spacing:0.5px;color:var(--navy)}
  .auth{position:absolute;right:63px;top:29px;display:flex;gap:7px}
  .btn{height:45px;width:117px;display:flex;align-items:center;justify-content:center;font-family:"Montserrat",sans-serif;font-weight:600;font-size:13px;border-radius:3px}
  .btn-outline{border:2px solid var(--brand);color:var(--brand);background:var(--white)}
  .btn-dark{background:var(--navy);color:var(--white)}

  .main-nav{position:absolute;left:0;top:102px;width:1200px;height:55px;background:var(--brand);display:flex;padding-left:74px}
  .main-nav a{font-family:"Montserrat",sans-serif;font-weight:600;font-size:13px;color:var(--white);text-decoration:none;display:flex;align-items:center;padding:0 27px}
  .main-nav a.active{background:var(--white);color:var(--brand);width:101px;justify-content:center;padding:0}

  .hero-visual{position:absolute;left:71px;top:196px;width:521px;height:402px;background:linear-gradient(135deg,#bdbdbd,#8e8e8e 55%,#a6a6a6)}

  .intro{position:absolute;left:654px;top:212px;width:480px}
  .intro h1{font-size:19px;font-weight:700}
  .intro p{font-family:"Quicksand",sans-serif;font-size:16px;color:var(--ink-soft);margin-top:6px}
  .rule{position:absolute;height:1px;background:var(--line)}

  .appt-title{position:absolute;left:654px;top:333px;font-size:17px;font-weight:700}
  .appt-form{position:absolute;left:654px;top:378px;width:484px;height:214px;background:var(--brand)}
  .field{position:absolute;height:47px;background:var(--white);border-radius:3px;font-family:"Quicksand",sans-serif;font-size:14px;color:#666;padding:15px 18px}
  .agree{position:absolute;left:16px;top:161px;display:flex;align-items:center;gap:7px;color:var(--white);font-family:"Quicksand",sans-serif;font-weight:500;font-size:14px}
  .agree i{width:13px;height:13px;background:var(--white);border-radius:2px;display:block}
  .submit{position:absolute;left:313px;top:142px;width:158px;height:53px;background:var(--navy);color:var(--white);border-radius:4px;font-size:17px;display:flex;align-items:center;justify-content:center}

  .section-title{position:absolute;top:683px;font-size:19px;font-weight:700}
  .tiles{position:absolute;left:71px;top:731px;display:flex;gap:14px}
  .tile{width:119px;height:110px;border-radius:2px}
  .tile.blue{background:var(--tile-blue)}
  .tile.yellow{background:var(--tile-yellow)}
  .tile.purple{background:var(--tile-purple)}
  .tile.sky{background:var(--tile-sky)}

  .reasons{position:absolute;left:660px;top:728px;width:480px;list-style:none}
  .reasons li{font-size:15px;line-height:20px;padding-left:16px;position:relative;margin-bottom:14px}
  .reasons li::before{content:"";position:absolute;left:0;top:7px;width:6px;height:6px;background:var(--brand)}
</style>
</head>
<body>
  <header class="site-header">
    <div class="social" aria-label="Socialni site"><span></span><span></span><span></span></div>
    <div class="brand">Krytona</div>
    <div class="auth">
      <a class="btn btn-outline">PRIHLASIT</a>
      <a class="btn btn-dark">PRIHLASIT</a>
    </div>
  </header>

  <nav class="main-nav">
    <a class="active">O NAS</a>
    <a>CASTE DOTAZE</a>
    <a>KONTAKE</a>
  </nav>

  <div class="hero-visual" role="img" aria-label="Illustration of a hand holding an umbrella over a sketched family, house and car under a stormy sky"></div>

  <section class="intro">
    <h1>Najdete Nejvyhodnejsi Pojisteni</h1>
    <p>Havarijnr Pojistene</p>
  </section>
  <div class="rule" style="left:654px;top:296px;width:480px"></div>

  <h2 class="appt-title">MAKE AN APPOINTMENT NOW!</h2>
  <form class="appt-form">
    <div class="field" style="left:14px;top:20px;width:235px">Jmeno *</div>
    <div class="field" style="left:263px;top:20px;width:207px">Prijmeni *</div>
    <div class="field" style="left:14px;top:79px;width:456px">Email *</div>
    <label class="agree"><i></i>Souhlasim S Podminkami&nbsp; Pouziti</label>
    <div class="submit">Spocitat Cenu</div>
  </form>

  <div class="rule" style="left:71px;top:647px;width:521px"></div>
  <div class="rule" style="left:654px;top:647px;width:480px"></div>

  <h2 class="section-title" style="left:71px">Chcete Pojistit Neco Jineho?</h2>
  <div class="tiles">
    <div class="tile blue"></div>
    <div class="tile yellow"></div>
    <div class="tile purple"></div>
    <div class="tile sky"></div>
  </div>

  <h2 class="section-title" style="left:660px">Proc Hledat Pojisteni Pres Krytona?</h2>
  <ul class="reasons">
    <li>Lorem ipsum dolor sit amet, consectetur adipiscing elit.</li>
    <li>Sed do eiusmod tempor incididunt ut labore et dolore.</li>
    <li>Ut enim ad minim veniam, quis nostrud exercitation.</li>
  </ul>
</body>
</html>
```